Wordpress Design Help

We are building a new website for a Data Back Up Company. We have bought a template as below that we are quite happy with but need some help on how to make it a little more punchy.
What we need is some concept on what we can do to make the website look better and more web 2.0, we do not require any coding or templates built. I have an excellent wordpress developer who can do this.
We also need some concepts for the & Day Free Trial Button
I just require high quality images to show the developer what to build.
We also require that the 7 Day Free Trial Image be sent separately (Please see attachment)
As below is the link for the template, also attached are screen shoots of how the website currently looks.
http://demos.lorabrix.com/tamuvo/
Target Market(s)
Small to medium sized business owners who have not reached the size to have thier own IT department yet. We come in and install out software which will do backups to an offsite server automatically for them
Industry/Entity Type
Building
Look and feel
Each slider illustrates characteristics of the customer's brand and the style your logo design should communicate.

```html
<!DOCTYPE html>
<html lang="en">
<head>
<meta charset="utf-8">
<title>Vaultline – Home</title>
<link rel="stylesheet" href="https://fonts.googleapis.com/css2?family=Open+Sans:wght@400;600;700&family=Arimo:ital,wght@0,400;0,700;1,400&display=swap">
<style>
:root{
  --bg:#1c1c1c;
  --panel:#f3f3f3;
  --white:#ffffff;
  --ink:#222222;
  --brand:#3fa34d;
  --green-top:#4cb447;
  --green-bot:#2a8a2a;
  --orange-top:#ffa238;
  --orange-bot:#f07400;
  --card:#4a4640;
  --card-text:#d8d4cc;
  --card-faint:#7a756d;
  --link-red:#8a1010;
  --footer-text:#bdbdbd;
  --social:#5a8fc8;
}
*{box-sizing:border-box;margin:0;padding:0}
html,body{width:1200px;height:1134px;overflow:hidden}
body{background:var(--bg);font-family:"Arimo",Arial,sans-serif;color:var(--ink);position:relative}
.site-header{position:absolute;left:0;top:0;width:1200px;height:96px;background:linear-gradient(#2e2e2e,#1a1a1a);border-bottom:1px solid #333}
.brand{position:absolute;left:82px;top:24px;display:flex;align-items:center;gap:12px;font-family:"Open Sans",sans-serif;font-weight:700;font-size:36px;color:var(--brand);letter-spacing:-0.5px}
.brand-mark{width:30px;height:30px;background:var(--brand)}
.search{position:absolute;left:927px;top:8px;width:194px;height:25px;background:var(--white);border-radius:3px;font-size:13px;color:#555;padding:5px 6px}
.search-btn{position:absolute;right:0;top:0;width:26px;height:25px;background:#2a7ee0;border-radius:0 3px 3px 0}
.main-nav{position:absolute;right:75px;top:50px;display:flex;gap:22px;font-family:"Open Sans",sans-serif;font-size:15px;color:var(--white)}
.main-nav span{padding:3px 8px}
.main-nav .current{border:1px solid #888;border-radius:3px;color:#bbb;background:#3a3a3a}
.hero{position:absolute;left:83px;top:113px;width:1040px;height:339px;background:var(--panel)}
.hero h1{position:absolute;left:10px;top:16px;font-family:"Open Sans",sans-serif;font-weight:400;font-size:29px;color:#555}
.hero-text{position:absolute;left:10px;top:58px;width:290px;font-style:italic;font-size:14.5px;line-height:22.5px;color:var(--ink);white-space:nowrap}
.hero-arrows{position:absolute;left:13px;top:306px;display:flex;gap:5px}
.hero-arrows span{width:28px;height:21px;background:#333;display:flex;align-items:center;justify-content:center}
.hero-media{position:absolute;left:314px;top:8px;width:714px;height:322px;border:1px solid #bbb;border-radius:3px;background:linear-gradient(135deg,#2a2a2a,#6d6d6d 45%,#c9c9c9 70%,#555);overflow:hidden}
.hero-caption{position:absolute;left:0;bottom:0;width:100%;height:63px;background:rgba(235,235,235,.85);padding:8px 14px;font-style:italic;font-size:14px;line-height:22px;color:#222}
.cta{position:absolute;left:83px;width:312px;height:83px;border-radius:4px;color:var(--white);text-align:center;font-family:"Open Sans",sans-serif;text-shadow:0 1px 2px rgba(0,0,0,.4)}
.cta small{display:block;font-size:26px;line-height:32px;padding-top:4px}
.cta strong{display:block;font-size:35px;line-height:42px;font-weight:600;white-space:nowrap}
.cta-trial{top:478px;background:linear-gradient(var(--green-top),var(--green-bot));border:2px solid #7fd27a}
.cta-pricing{top:579px;background:linear-gradient(var(--orange-top),var(--orange-bot));border:2px solid #ffc07a}
.intro{position:absolute;left:406px;top:478px;width:717px;height:184px;background:var(--white);padding:8px 34px}
.intro h2{font-family:"Open Sans",sans-serif;font-weight:600;font-size:18px;color:#333;margin-bottom:8px}
.intro p{font-size:14px;line-height:22.5px;padding-left:4px}
.read-more{position:absolute;right:30px;bottom:24px;font-size:14px;color:var(--link-red);display:flex;align-items:center;gap:8px}
.read-more svg{width:6px;height:10px}
.card{position:absolute;top:693px;width:328px;height:314px;background:var(--card);padding:8px}
.card h3{font-family:"Open Sans",sans-serif;font-weight:600;font-size:20px;color:var(--white);padding-bottom:6px;border-bottom:1px dotted #aaa;margin-bottom:10px}
.card-thumb{float:left;width:153px;height:128px;background:var(--white);border:1px solid #ddd;margin-right:8px;padding:6px}
.card-thumb div{width:100%;height:100%}
.card p{font-size:11.5px;line-height:13.5px;text-align:justify;color:var(--card-text)}
.card p.faint{color:var(--card-faint)}
.card .lead{margin-bottom:2px}
.card-btn{position:absolute;left:10px;bottom:22px;width:92px;height:24px;border:1px solid #999;color:var(--white);font-size:12px;text-align:center;line-height:22px}
.site-footer{position:absolute;left:0;top:1063px;width:1200px;height:71px;border-top:1px solid #333;background:#1a1a1a}
.copyright{position:absolute;left:93px;top:15px;font-size:12px;color:var(--footer-text)}
.footer-nav{position:absolute;left:93px;top:40px;font-size:12px;color:var(--footer-text)}
.footer-nav span{margin:0 6px}
.social{position:absolute;right:76px;top:25px;display:flex;gap:12px}
.social span{width:26px;height:26px;background:var(--social);border-radius:3px}
</style>
</head>
<body>
<header class="site-header">
  <div class="brand"><span class="brand-mark"></span>VAULTLINE</div>
  <div class="search">Search<span class="search-btn"></span></div>
  <nav class="main-nav">
    <span class="current">HOME</span><span>WHAT WE DO</span><span>DOWNLOADS</span><span>GET A QUOTE</span><span>BLOG</span><span>CONTACT US</span>
  </nav>
</header>

<section class="hero">
  <h1>What is Vaultline</h1>
  <p class="hero-text">The software is Hartwell Terminal HT<br>(HT Terminal Emulator for Desktop).<br>That software is edn of the line and no<br>longer supported, so upward compatibil-<br>ity for this server is nil.<br>The software is Hartwell Terminal HT<br>(HT Terminal Emulator for Desktop).<br>That software is edn of the line and no<br>longer supported, so upward compatibil-<br>ity for this server is nil.</p>
  <div class="hero-arrows">
    <span><svg width="18" height="10" viewBox="0 0 18 10"><path d="M0 5h16M12 1l4 4-4 4" stroke="#fff" stroke-width="1.5" fill="none"/></svg></span>
    <span><svg width="18" height="10" viewBox="0 0 18 10"><path d="M18 5H2M6 1L2 5l4 4" stroke="#fff" stroke-width="1.5" fill="none"/></svg></span>
  </div>
  <div class="hero-media" role="img" aria-label="Photo of miniature workers repairing an open hard drive">
    <p class="hero-caption">Phasellus fringilla vehicula egestas. Class aptent taciti sociosqu ad litora torquent per conubia nostra, per inceptos himenaeos. Nam</p>
  </div>
</section>

<div class="cta cta-trial"><small>Try our 7 Day</small><strong>FREE TRIAL</strong></div>
<div class="cta cta-pricing"><small>See our</small><strong>PLAN &amp; PRICING</strong></div>

<section class="intro">
  <h2>Vaultline - Smart Data Protection for Professionals,Corporate’s</h2>
  <p>The software is Hartwell Terminal HT (HT Terminal Emulator for Desktop).<br>That software is edn of the line and no longer supported, so upward compatibility for this server is nil.<br>The software is Hartwell Terminal HT (HT Terminal Emulator for Desktop).<br>That software is edn of the line and no longer supported, so upward compatibility for this server is nil.</p>
  <div class="read-more"><svg viewBox="0 0 6 10"><path d="M0 0l6 5-6 5z" fill="#8a1010"/></svg>Read More</div>
</section>

<article class="card" style="left:83px">
  <h3>Featured Product</h3>
  <div class="card-thumb"><div role="img" aria-label="Illustration of a drive with sync arrows and a disc" style="background:linear-gradient(135deg,#7fcf5a,#d8d8d8)"></div></div>
  <p class="lead">"I initially selected Northfield Small Business product only because of the brand name, but later on realized that the product is very useful and user friendly. The tools and templates which have been provided by Northfield Small Business are very..."</p>
  <p>"I initially selected Northfield Small Business product only because of the brand name, but later on realized that the product is very useful and user friendly. The tools and templates which have been provided by Northfield Small Business are very..."</p>
  <div class="card-btn">READ MORE</div>
</article>

<article class="card" style="left:440px">
  <h3>Offsite Data Protection</h3>
  <div class="card-thumb"><div role="img" aria-label="Illustration of a laptop with a wrench and screwdriver" style="background:linear-gradient(135deg,#cfd8e0,#6a8fb0 60%,#333)"></div></div>
  <p class="lead faint">"I initially selected Northfield Small Business product only because of the brand name, but later on realized that the product is very useful and user friendly. The tools and templates which have been provided by Northfield Small Business are very..."</p>
  <p class="faint">"I initially selected Northfield Small Business product only because of the brand name, but later on realized that the product is very useful and user friendly. The tools and templates which have been provided by Northfield Small Business are very..."</p>
  <div class="card-btn">READ MORE</div>
</article>

<article class="card" style="left:795px">
  <h3>Remote Data Protection</h3>
  <div class="card-thumb"><div role="img" aria-label="Illustration of a silver database stack with a magnifying glass" style="background:linear-gradient(135deg,#f0f0f0,#9c9c9c 60%,#4a9fd8)"></div></div>
  <p class="lead">"I initially selected Northfield Small Business product only because of the brand name, but later on realized that the product is very useful and user friendly. The tools and templates which have been provided by Northfield Small Business are very..."</p>
  <p>"I initially selected Northfield Small Business product only because of the brand name, but later on realized that the product is very useful and user friendly. The tools and templates which have been provided by Northfield Small Business are very..."</p>
  <div class="card-btn">READ MORE</div>
</article>

<footer class="site-footer">
  <p class="copyright">Copyright © Vaultline.example 2011. All rights reserved.</p>
  <p class="footer-nav">Home<span>|</span>What We Do<span>|</span>Downloads<span>|</span>Get a quote<span>|</span>Blog<span>|</span>Site Map<span>|</span>Contact Us</p>
  <div class="social"><span aria-label="Social profile"></span><span aria-label="Social profile"></span></div>
</footer>
</body>
</html>
```